IT Company based on Biology Business Needs a Business Card Design

We need a business card design for a new company called 'Lumen CELL'. We develop the machine learning solutions especially focused on deep learning algorithms for biology industry. Our initial product is a vision detection on biological images to help doctors diagnose the symptoms. We would like to see designs that use the color green.

Industry/Entity Type

Business

```html
<!DOCTYPE html>
<html lang="en">
<head>
<meta charset="utf-8">
<title>Lumen CELL – Business Card</title>
<link rel="stylesheet" href="https://fonts.googleapis.com/css2?family=Questrial&display=swap">
<style>
  :root {
    --page-bg: #e4e5e6;
    --card-white: #f4f4f5;
    --brand-green: #67a839;
    --brand-green-dark: #0f7a3d;
    --text-grey: #555659;
    --on-green: #eef5e8;
  }
  html, body {
    margin: 0;
    padding: 0;
    width: 1105px;
    height: 1200px;
    overflow: hidden;
    background: var(--page-bg);
    font-family: "Questrial", "Century Gothic", sans-serif;
  }
  .canvas {
    position: relative;
    width: 1105px;
    height: 1200px;
  }
  .card {
    position: absolute;
    left: 179px;
    width: 747px;
    height: 427px;
    box-shadow: 0 10px 22px rgba(0,0,0,0.22);
    overflow: hidden;
  }
  .card-front { top: 119px; background: var(--card-white); }
  .card-back { top: 635px; background: var(--brand-green); }

  .edge-band { position: absolute; left: 0; top: 0; }

  .brand-name {
    position: absolute;
    left: 76px;
    top: 56px;
    margin: 0;
    font-size: 42px;
    font-weight: 400;
    color: var(--brand-green);
    letter-spacing: -0.5px;
    display: flex;
    align-items: center;
    gap: 14px;
  }
  .brand-dot {
    width: 20px;
    height: 20px;
    border-radius: 50%;
    background: var(--brand-green-dark);
  }

  .address {
    position: absolute;
    left: 76px;
    top: 196px;
    margin: 0;
    font-style: normal;
    font-size: 21px;
    line-height: 28px;
    color: var(--text-grey);
  }
  .contact-list {
    position: absolute;
    left: 76px;
    top: 263px;
    margin: 0;
    padding: 0;
    list-style: none;
    font-size: 21px;
    color: var(--text-grey);
  }
  .contact-list li {
    display: flex;
    align-items: center;
    height: 32px;
  }
  .contact-icon {
    width: 20px;
    height: 20px;
    margin-right: 14px;
    fill: var(--brand-green);
  }

  .person {
    position: absolute;
    right: 36px;
    top: 238px;
    text-align: right;
    color: var(--brand-green);
  }
  .person-name {
    margin: 0;
    font-size: 26px;
    font-weight: 400;
    letter-spacing: 0.5px;
    -webkit-text-stroke: 0.6px var(--brand-green);
  }
  .person-role {
    margin: 4px 0 0;
    font-size: 21px;
  }

  .back-brand {
    position: absolute;
    left: 0;
    right: 0;
    top: 170px;
    display: flex;
    justify-content: center;
    align-items: center;
    gap: 16px;
    font-size: 48px;
    color: var(--on-green);
  }
  .back-dot {
    width: 24px;
    height: 24px;
    border-radius: 50%;
    background: var(--on-green);
  }
  .social-handle {
    position: absolute;
    left: 0;
    right: 0;
    top: 347px;
    text-align: center;
    font-size: 20px;
    color: var(--on-green);
    letter-spacing: 1px;
  }
</style>
</head>
<body>
<div class="canvas">

  <section class="card card-front">
    <svg class="edge-band" width="60" height="427" viewBox="0 0 60 427" aria-hidden="true">
      <rect x="0" y="0" width="34" height="108" fill="var(--brand-green-dark)"/>
      <polygon points="0,110 34,110 46,100 46,106 34,118 34,427 0,427" fill="var(--brand-green)"/>
    </svg>

    <h1 class="brand-name"><span class="brand-dot"></span>Lumen CELL</h1>

    <address class="address">214 Fernbrook Road<br>Juneau, Alaska 99801</address>

    <ul class="contact-list">
      <li>
        <svg class="contact-icon" viewBox="0 0 24 24" aria-hidden="true"><path d="M6.6 10.8a15.1 15.1 0 0 0 6.6 6.6l2.2-2.2a1 1 0 0 1 1-.25 11.4 11.4 0 0 0 3.6.57 1 1 0 0 1 1 1V20a1 1 0 0 1-1 1A17 17 0 0 1 3 4a1 1 0 0 1 1-1h3.5a1 1 0 0 1 1 1c0 1.25.2 2.45.57 3.57a1 1 0 0 1-.25 1z"/></svg>
        555 210 4471
      </li>
      <li>
        <svg class="contact-icon" viewBox="0 0 24 24" aria-hidden="true"><path d="M7 1h10a2 2 0 0 1 2 2v18a2 2 0 0 1-2 2H7a2 2 0 0 1-2-2V3a2 2 0 0 1 2-2zm0 3v14h10V4zm5 15.5a1 1 0 1 0 0 2 1 1 0 0 0 0-2z"/></svg>
        555 390 8126
      </li>
      <li>
        <svg class="contact-icon" viewBox="0 0 24 24" aria-hidden="true"><path d="M2 6h20v12H2zm2 1.5 8 5.5 8-5.5V7H4z"/></svg>
        hello@lumencell.io
      </li>
      <li>
        <svg class="contact-icon" viewBox="0 0 24 24" aria-hidden="true"><circle cx="12" cy="12" r="10"/><path d="M12 2a10 10 0 0 0 0 20M2 12h20M12 2c3 3 3 17 0 20" fill="none" stroke="var(--card-white)" stroke-width="1.4"/></svg>
        www.lumencell.io
      </li>
    </ul>

    <div class="person">
      <h2 class="person-name">MARA LINDQVIST</h2>
      <p class="person-role">CEO/Founder</p>
    </div>
  </section>

  <section class="card card-back">
    <div class="back-brand"><span class="back-dot"></span>Lumen CELL</div>
    <p class="social-handle">@lumencell</p>
  </section>

</div>
</body>
</html>
```